Kitchen manufaturer business card/logo design

I am a small kitchen manufacturing company that makes and installs all sorts of cabinetry.

The colours im looking to incorporate in the card are light/baby blue, white and black.

Incorporate 5 stars to show quality workmanship and product.

Looking for a modern classy design.
Updates

Hey guys, New idea. The logo should be made using HK in the most modern way possible as well as the full company name below it. Thanks.

Target Market(s)

Anyone with a home thats looking for a new cabinetry of any sort.

Industry/Entity Type

Business

Contact Information for Business Card

Harbor Kitchens
Tod Villaran
PH 0431 582 904
Email- harborkitchens@mailvane.example
ABN- 73 208 561 339
-Kitchens
-Vanities
-Laundries
-Media Units
-Studies
-Wardrobes
-3D Computer Designs

Requirements
Must have

• The front of the card must only have the company name.
The different types of cabinetry I do must be on the back of the card in point form but instead of using points use stars.
Nice to have
• Just think classy and quality

```html
<!DOCTYPE html>
<html lang="en">
<head>
<meta charset="utf-8">
<title>Harbor Kitchens – Business Card Back</title>
<link rel="stylesheet" href="https://fonts.googleapis.com/css2?family=Pinyon+Script&family=Roboto:wght@300;400&display=swap">
<style>
  :root {
    --sky-light: #3cc3f2;
    --sky-mid: #14a4dc;
    --sky-deep: #0a86c0;
    --charcoal-light: #6e6e6e;
    --charcoal-mid: #3a3a3a;
    --charcoal-deep: #050505;
    --ink-white: #ffffff;
    --ink-grey: #d6d6d6;
    --contact-ink: #0b1a26;
    --edge-glow: #cfefff;
  }
  html, body {
    margin: 0;
    padding: 0;
    width: 1200px;
    height: 741px;
    overflow: hidden;
    background: #ffffff;
  }
  .card {
    position: relative;
    width: 1200px;
    height: 741px;
    overflow: hidden;
    font-family: "Roboto", "Helvetica Neue", Arial, sans-serif;
  }
  .card__backdrop {
    position: absolute;
    inset: 0;
    width: 1200px;
    height: 741px;
  }
  .owner-name {
    position: absolute;
    left: 30px;
    top: 300px;
    width: 612px;
    margin: 0;
    text-align: center;
    font-family: "Pinyon Script", cursive;
    font-weight: 400;
    font-size: 108px;
    line-height: 1;
    color: var(--ink-white);
    white-space: nowrap;
    text-shadow: 2px 3px 3px rgba(0, 30, 60, 0.75);
  }
  .contact {
    position: absolute;
    left: 70px;
    top: 560px;
    margin: 0;
    padding: 0;
    list-style: none;
  }
  .contact__item {
    display: flex;
    align-items: center;
    height: 54px;
    font-weight: 300;
    color: var(--contact-ink);
    white-space: nowrap;
  }
  .contact__item--phone { font-size: 36px; }
  .contact__item--email { font-size: 32px; letter-spacing: -0.5px; }
  .contact__icon {
    width: 32px;
    height: 32px;
    margin-right: 15px;
    flex: none;
  }
  .services {
    position: absolute;
    left: 680px;
    top: 119px;
    margin: 0;
    padding: 0;
    list-style: none;
  }
  .services__item {
    display: flex;
    align-items: center;
    height: 68.5px;
    font-size: 41px;
    font-weight: 300;
    color: var(--ink-white);
    white-space: nowrap;
  }
  .services__star {
    width: 38px;
    height: 38px;
    margin-right: 6px;
    flex: none;
  }
  .abn {
    position: absolute;
    left: 724px;
    top: 630px;
    margin: 0;
    font-size: 40px;
    font-weight: 300;
    line-height: 48px;
    color: var(--ink-grey);
    white-space: nowrap;
  }
</style>
</head>
<body>
<main class="card">
  <svg class="card__backdrop" viewBox="0 0 1200 741" aria-hidden="true">
    <defs>
      <linearGradient id="charcoal-fill" x1="0" y1="0" x2="1" y2="1">
        <stop offset="0" stop-color="var(--charcoal-light)"/>
        <stop offset="0.45" stop-color="var(--charcoal-mid)"/>
        <stop offset="1" stop-color="var(--charcoal-deep)"/>
      </linearGradient>
      <linearGradient id="sky-fill" x1="0" y1="0" x2="0.3" y2="1">
        <stop offset="0" stop-color="var(--sky-light)"/>
        <stop offset="0.55" stop-color="var(--sky-mid)"/>
        <stop offset="1" stop-color="var(--sky-deep)"/>
      </linearGradient>
      <linearGradient id="star-metal" x1="0" y1="0" x2="1" y2="1">
        <stop offset="0" stop-color="#ffffff"/>
        <stop offset="0.5" stop-color="#a9a9a9"/>
        <stop offset="1" stop-color="#5a5a5a"/>
      </linearGradient>
      <symbol id="silver-star" viewBox="0 0 36 36">
        <polygon points="18,2 22.7,13.5 35,14 25.5,21.8 28.8,34 18,27 7.2,34 10.5,21.8 1,14 13.3,13.5" fill="url(#star-metal)" stroke="#ffffff" stroke-opacity="0.6" stroke-width="0.8"/>
      </symbol>
    </defs>
    <rect class="panel-dark" width="1200" height="741" fill="url(#charcoal-fill)"/>
    <path class="panel-blue" d="M0 0 H435 C560 130 660 330 655 480 C652 600 600 690 548 741 H0 Z" fill="url(#sky-fill)"/>
    <path class="panel-edge" d="M435 0 C560 130 660 330 655 480 C652 600 600 690 548 741" fill="none" stroke="var(--edge-glow)" stroke-opacity="0.7" stroke-width="2"/>
  </svg>

  <h1 class="owner-name">Tod Villaran</h1>

  <ul class="contact">
    <li class="contact__item contact__item--phone">
      <svg class="contact__icon" viewBox="0 0 24 24" aria-hidden="true">
        <path d="M6.6 2.5c.6-.3 1.3-.1 1.6.5l2 3.8c.3.6.2 1.2-.3 1.6l-1.5 1.2c.9 2 2.6 3.8 4.6 4.8l1.3-1.5c.4-.5 1.1-.6 1.6-.3l3.7 2.1c.6.3.8 1 .5 1.6l-1.2 2.3c-.5.9-1.5 1.4-2.5 1.2C9.3 18.7 4.6 13.2 3.6 6.2c-.1-1 .4-2 1.3-2.5z" fill="var(--contact-ink)"/>
      </svg>
      <span>0431 582 904</span>
    </li>
    <li class="contact__item contact__item--email">
      <svg class="contact__icon" viewBox="0 0 24 24" aria-hidden="true">
        <g fill="none" stroke="var(--contact-ink)" stroke-width="1.6" stroke-linejoin="round">
          <path d="M2.5 10 L12 3.5 L21.5 10 V20.5 H2.5 Z"/>
          <path d="M2.5 10 L12 16 L21.5 10"/>
          <path d="M2.5 20.5 L9.5 14.5 M21.5 20.5 L14.5 14.5"/>
        </g>
      </svg>
      <span>harborkitchens@mailvane.example</span>
    </li>
  </ul>

  <ul class="services">
    <li class="services__item"><svg class="services__star" aria-hidden="true"><use href="#silver-star"/></svg>Kitchens</li>
    <li class="services__item"><svg class="services__star" aria-hidden="true"><use href="#silver-star"/></svg>Vanities</li>
    <li class="services__item"><svg class="services__star" aria-hidden="true"><use href="#silver-star"/></svg>Laundries</li>
    <li class="services__item"><svg class="services__star" aria-hidden="true"><use href="#silver-star"/></svg>Media Units</li>
    <li class="services__item"><svg class="services__star" aria-hidden="true"><use href="#silver-star"/></svg>Studies</li>
    <li class="services__item"><svg class="services__star" aria-hidden="true"><use href="#silver-star"/></svg>Wardrobes</li>
    <li class="services__item"><svg class="services__star" aria-hidden="true"><use href="#silver-star"/></svg>3D Computer Designs</li>
  </ul>

  <p class="abn">ABN- 73 208 561 339</p>
</main>
</body>
</html>
```